Lorna Tess Tresses Fancy Business Card’s

I want my business cards to be elite, original and very classy. I want the business cards to match the colors of my logo and to match the design posted. I would love the design of the picture I posted

I want the card all white .
The dripping on the top of the card I want it to match the pink color in my logo that’s also posted .
I need my logo on the business card !
I need my Instagram- @lorna.tess.tresses__
And my phone number - 582 907 3365

Target Market(s)

My target market is young woman age 23 to older woman to the age of 65
I want both older and younger women to love my design . I don’t want any cheap looking business cards

Industry/Entity Type

Hair And Beauty

Contact Information for Business Card

Add my logo
Add my Instagram- @lorna.tess.tresses__
My number - 582 907 3365
My website- www.lornatesstresses.example

Font styles to use
Serif
Script

Colors
ffffff
e667a6
e34298

Requirements
Must have
• The business cards must have my logo, my number , my website, and my Instagram!
Nice to have
• Nice to have glitter words that match my logo
• The business cards must look classy and mature
• I want them to be very unique!!
Should not have
• Should not have any colors that doesn’t match my logo ! This is very important! Please

```html
<!DOCTYPE html>
<html lang="en">
<head>
<meta charset="utf-8">
<title>Lorna Tess Tresses – Business Cards</title>
<link rel="stylesheet" href="https://fonts.googleapis.com/css2?family=Playfair+Display:wght@400&family=Roboto:wght@300&display=swap">
<style>
  :root {
    --white: #ffffff;
    --page: #e9e9ea;
    --pink-light: #e667a6;
    --pink-deep: #e34298;
    --silver-dark: #9a9a9c;
    --silver-light: #f2f2f2;
    --ink-grey: #8f8f92;
  }
  html, body {
    margin: 0;
    padding: 0;
    width: 1200px;
    height: 1200px;
    overflow: hidden;
    background: var(--page);
  }
  .canvas {
    position: relative;
    width: 1200px;
    height: 1200px;
  }
  .card {
    position: absolute;
    left: 223px;
    width: 754px;
    height: 451px;
    background: var(--white);
  }
  .card--front { top: 112px; }
  .card--back  { top: 637px; }
  .card svg {
    display: block;
    width: 100%;
    height: 100%;
  }
  .brand-name {
    font-family: "Playfair Display", Georgia, serif;
    font-weight: 400;
    fill: var(--pink-deep);
  }
  .contact-text {
    font-family: "Roboto", Arial, sans-serif;
    font-weight: 300;
    font-size: 40px;
    fill: var(--ink-grey);
  }
  .contact-icon {
    fill: none;
    stroke: var(--pink-deep);
    stroke-width: 4;
    stroke-linecap: round;
    stroke-linejoin: round;
  }
  .band-solid   { fill: var(--pink-light); }
  .band-glitter { fill: var(--pink-deep); }
</style>
</head>
<body>
<main class="canvas">

  <!-- Front of card -->
  <section class="card card--front" aria-label="Business card front">
    <svg viewBox="0 0 1214 726" preserveAspectRatio="none">
      <defs>
        <linearGradient id="silver-front" x1="0" y1="0" x2="1" y2="1">
          <stop offset="0" stop-color="var(--silver-dark)"/>
          <stop offset="0.5" stop-color="var(--silver-light)"/>
          <stop offset="1" stop-color="var(--silver-dark)"/>
        </linearGradient>
        <linearGradient id="fade-tl" x1="0" y1="0" x2="0.6" y2="0.6">
          <stop offset="0" stop-color="#cfcfd1"/>
          <stop offset="1" stop-color="#ffffff" stop-opacity="0"/>
        </linearGradient>
        <linearGradient id="fade-br" x1="1" y1="1" x2="0.4" y2="0.4">
          <stop offset="0" stop-color="#cfcfd1"/>
          <stop offset="1" stop-color="#ffffff" stop-opacity="0"/>
        </linearGradient>
      </defs>

      <g class="corner-band corner-band--top-left">
        <path d="M270,0 L700,0 Q250,60 0,340 L0,140 Q110,60 270,0 Z" fill="url(#fade-tl)"/>
        <path class="band-solid" d="M0,0 L85,0 Q40,20 0,50 Z"/>
        <path class="band-glitter" d="M85,0 L210,0 Q90,45 0,115 L0,50 Q40,20 85,0 Z"/>
        <path d="M210,0 L270,0 Q110,60 0,140 L0,115 Q90,45 210,0 Z" fill="url(#silver-front)"/>
      </g>

      <g class="corner-band corner-band--bottom-right">
        <path d="M1214,420 Q950,640 720,726 L795,726 Q1000,650 1214,515 Z" fill="url(#fade-br)"/>
        <path d="M1214,515 Q1000,650 795,726 L865,726 Q1050,660 1214,540 Z" fill="url(#silver-front)"/>
        <path class="band-glitter" d="M1214,540 Q1050,660 865,726 L1020,726 Q1130,680 1214,630 Z"/>
        <path d="M1214,630 Q1130,680 1020,726 L1060,726 Q1140,690 1214,655 Z" fill="url(#silver-front)"/>
        <path class="band-solid" d="M1214,655 Q1140,690 1060,726 L1214,726 Z"/>
      </g>

      <text class="brand-name" x="607" y="395" font-size="84" text-anchor="middle">Lorna Tess Tresses</text>
    </svg>
  </section>

  <!-- Back of card -->
  <section class="card card--back" aria-label="Business card back">
    <svg viewBox="0 0 1214 726" preserveAspectRatio="none">
      <defs>
        <linearGradient id="silver-back" x1="0" y1="0" x2="1" y2="1">
          <stop offset="0" stop-color="var(--silver-dark)"/>
          <stop offset="0.5" stop-color="var(--silver-light)"/>
          <stop offset="1" stop-color="var(--silver-dark)"/>
        </linearGradient>
        <linearGradient id="fade-tl-back" x1="0" y1="0" x2="0.6" y2="0.6">
          <stop offset="0" stop-color="#cfcfd1"/>
          <stop offset="1" stop-color="#ffffff" stop-opacity="0"/>
        </linearGradient>
        <linearGradient id="fade-br-back" x1="1" y1="1" x2="0.4" y2="0.4">
          <stop offset="0" stop-color="#cfcfd1"/>
          <stop offset="1" stop-color="#ffffff" stop-opacity="0"/>
        </linearGradient>
        <radialGradient id="logo-shadow" cx="0.5" cy="0" r="0.5" gradientTransform="scale(1,0.3)">
          <stop offset="0" stop-color="#d6d6d8"/>
          <stop offset="1" stop-color="#ffffff" stop-opacity="0"/>
        </radialGradient>
      </defs>

      <g class="corner-band corner-band--top-left">
        <path d="M540,0 L820,0 Q300,80 0,360 L0,260 Q230,90 540,0 Z" fill="url(#fade-tl-back)"/>
        <path class="band-solid" d="M0,0 L260,0 Q120,45 0,120 Z"/>
        <path class="band-glitter" d="M260,0 L450,0 Q200,80 0,230 L0,120 Q120,45 260,0 Z"/>
        <path d="M450,0 L540,0 Q230,90 0,260 L0,230 Q200,80 450,0 Z" fill="url(#silver-back)"/>
      </g>

      <g class="corner-band corner-band--bottom-right">
        <path d="M1214,470 Q1000,650 790,726 L850,726 Q1030,660 1214,550 Z" fill="url(#fade-br-back)"/>
        <path d="M1214,550 Q1030,660 850,726 L920,726 Q1080,665 1214,575 Z" fill="url(#silver-back)"/>
        <path class="band-glitter" d="M1214,575 Q1080,665 920,726 L1070,726 Q1150,700 1214,675 Z"/>
        <path d="M1214,675 Q1150,700 1070,726 L1100,726 Q1160,708 1214,690 Z" fill="url(#silver-back)"/>
        <path class="band-solid" d="M1214,690 Q1160,708 1100,726 L1214,726 Z"/>
      </g>

      <text class="brand-name" x="576" y="200" font-size="74" text-anchor="middle">Lorna Tess Tresses</text>

      <rect class="logo-shadow" x="290" y="355" width="620" height="90" fill="url(#logo-shadow)"/>

      <g class="contact-list">
        <g class="contact-item contact-item--phone">
          <path class="contact-icon" d="M372,460 q-6,0 -6,8 q2,20 18,34 q14,14 32,16 q8,0 8,-6 l0,-8 q0,-4 -4,-5 l-10,-3 q-4,-1 -6,2 l-4,4 q-12,-6 -20,-18 l4,-4 q3,-3 2,-7 l-3,-10 q-1,-4 -5,-4 Z"/>
          <text class="contact-text" x="446" y="498">582 907 3365</text>
        </g>
        <g class="contact-item contact-item--social">
          <rect class="contact-icon" x="364" y="523" width="44" height="44" rx="12"/>
          <text class="contact-text" x="446" y="560">@lorna.tess.tresses__</text>
        </g>
        <g class="contact-item contact-item--web">
          <circle class="contact-icon" cx="386" cy="607" r="22"/>
          <text class="contact-text" x="446" y="621">www.lornatesstresses.example</text>
        </g>
      </g>
    </svg>
  </section>

</main>
</body>
</html>
```